Pillcartondepot

We have roughly 50 items that we will be trading online. They are medical products aimed at the US and UK markets.

Most will be in cuboid boxes.

We would to have our own design that we could use across the product range.

Target Market(s)

Us and uk patients. Often 30+ years old

Industry/Entity Type

Medical

Requirements
Must have
• Our logo and space to have the medical in the centre of the box so it is clearly visible.
Nice to have
• Nice and simple colour scheme, nothing too bold.

```html
<!DOCTYPE html>
<html lang="en">
<head>
<meta charset="utf-8">
<title>Pillcartondepot – Carton Panels</title>
<link rel="stylesheet" href="https://fonts.googleapis.com/css2?family=Questrial&display=swap">
<style>
  :root {
    --page: #ffffff;
    --panel: #f7f7f7;
    --panel-edge: #dcdcdc;
    --ink: #1b1b1b;
    --ink-soft: #6f6f6f;
    --brand-red: #b3202a;
    --blue: #1579c4;
    --blue-light: #3fa3e0;
    --blue-dark: #0b5ea8;
    --white: #ffffff;
  }
  * { box-sizing: border-box; margin: 0; padding: 0; }
  html, body { width: 1200px; height: 811px; overflow: hidden; background: var(--page); }
  body { font-family: "Questrial", sans-serif; color: var(--ink); position: relative; }

  .carton { position: absolute; left: 170px; top: 30px; width: 860px; height: 750px; }

  .panel { position: absolute; background: var(--panel); border: 1px solid var(--panel-edge); overflow: hidden; }

  /* top flap */
  .top-flap { left: 300px; top: 0; width: 560px; height: 120px; border-bottom: none;
              display: flex; align-items: center; justify-content: center; }
  .flap-brand { display: flex; align-items: center; gap: 8px; font-size: 22px; color: var(--brand-red); }
  .flap-brand .brand-dot { width: 15px; height: 15px; }

  /* side panel */
  .side-panel { left: 0; top: 120px; width: 300px; height: 630px; padding: 80px 18px 0 22px; border-right: none; }
  .info-block { margin-bottom: 30px; }
  .info-heading { font-size: 10px; color: var(--blue); margin-bottom: 7px; }
  .info-line { font-size: 8.5px; color: var(--ink-soft); line-height: 13px; white-space: nowrap; }

  /* front panel */
  .front-panel { left: 300px; top: 120px; width: 560px; height: 630px; }
  .brand { position: absolute; top: 26px; right: 26px; display: flex; align-items: center; gap: 6px;
           font-size: 17px; color: var(--brand-red); }
  .brand-dot { width: 12px; height: 12px; border-radius: 50%; background: var(--brand-red); flex: none; }

  .product-name { position: absolute; left: 34px; top: 88px; font-size: 46px; font-weight: 400; color: var(--ink); }
  .net-weight { position: absolute; right: 42px; top: 92px; font-size: 34px; color: #555; }

  .rule { position: absolute; left: 34px; right: 24px; top: 196px; height: 5px;
          background: linear-gradient(90deg, var(--blue-light), var(--blue) 70%, var(--blue-dark)); }

  .tagline { position: absolute; left: 34px; top: 214px; font-size: 21px; color: var(--blue); }
  .description { position: absolute; left: 34px; top: 250px; font-size: 14.5px; line-height: 21px; color: var(--ink-soft); }

  .band { position: absolute; left: 0; right: 0; top: 378px; bottom: 0;
          background: linear-gradient(100deg, var(--blue-light) 0%, var(--blue) 45%, var(--blue-dark) 100%); }
  .pack-count { position: absolute; right: 44px; bottom: 60px; font-size: 34px; color: var(--white); }
  .origin { position: absolute; left: 26px; bottom: 26px; font-size: 12px; line-height: 16px; color: var(--white); }
</style>
</head>
<body>
  <div class="carton">
    <section class="panel top-flap">
      <div class="flap-brand"><span class="brand-dot"></span>Pillcartondepot</div>
    </section>

    <section class="panel side-panel">
      <div class="info-block">
        <p class="info-heading">Lorem ipsum ad his scripta blandit partiendo,</p>
        <p class="info-line">Lorem ipsum ad his scripta blandit partiendo,</p>
        <p class="info-line">eum Fastidii accumsan euripidis in, eum liber</p>
        <p class="info-line">Lorem ipsum ad his scripta blandit partiendo,</p>
        <p class="info-line">eum Fastidii accumsan euripidis in, eum liber</p>
      </div>
      <div class="info-block">
        <p class="info-heading">Lorem ipsum</p>
        <p class="info-line">Lorem ipsum ad his scripta blandit partiendo,</p>
        <p class="info-line">eum Fastidii accumsan euripidis in, eum liber</p>
        <p class="info-line">hendrerit an.</p>
      </div>
      <div class="info-block">
        <p class="info-heading">Lorem ipsum</p>
        <p class="info-line">Lorem ipsum ad his scripta blandit partiendo,</p>
        <p class="info-line">eum Fastidii accumsan euripidis in, eum liber</p>
        <p class="info-line">hendrerit an.</p>
      </div>
      <div class="info-block">
        <p class="info-heading">Lorem ipsum</p>
        <p class="info-line">Lorem ipsum ad his scripta blandit partiendo,</p>
        <p class="info-line">eum Fastidii accumsan euripidis in, eum liber</p>
        <p class="info-line">hendrerit an.</p>
      </div>
    </section>

    <section class="panel front-panel">
      <div class="brand"><span class="brand-dot"></span>Pillcartondepot</div>
      <h1 class="product-name">Lorem Ipsum</h1>
      <p class="net-weight">40g</p>
      <div class="rule"></div>
      <p class="tagline">Lorem ipsum ad his scripta blandit</p>
      <p class="description">Lorem ipsum ad his scripta blandit partiendo,<br>eum Fastidii accumsan euripidis in, eum liber hendrerit an</p>
      <div class="band">
        <p class="pack-count">24</p>
        <p class="origin">Original Flavour<br>Made In Australia</p>
      </div>
    </section>
  </div>
</body>
</html>
```